Healer at the Hearth needs business card

We need a business card that reflects the look and feel of the new website at www.healerathearth.ca

Target Market(s)

Our patient navigation and advocacy services are most commonly used by seniors who feel overwhelmed by the health care system and want someone on their side to advocate for their care. Individuals with ill parents or other family members may also come to rely on Healer at the Hearth to help them support their loved one through their health care journey. Ultimately, anyone who finds their health care experience challenging and wants someone completely focused on their needs can benefit from the services of our doctor / nurse team.

Industry/Entity Type

Business

Requirements
Must have
• One design tailored for two clinician which should include: logo, name, title, tel, email, web address and tagline
Nice to have
• A banner image to create a similar look to the website at www.healerathearth.ca
Should not have
• Too cluttered or busy - must be clean and professional

```html
<!DOCTYPE html>
<html lang="en">
<head>
<meta charset="utf-8">
<title>Healer at the Hearth — Business Card</title>
<link rel="stylesheet" href="https://fonts.googleapis.com/css2?family=Fira+Sans:wght@300;400&family=Jost:wght@400;500&display=swap">
<style>
  :root {
    --backdrop: #a7a8ab;
    --brand-blue: #02668f;
    --brand-blue-deep: #015a7e;
    --brand-red: #a3171f;
    --ink: #3a3a3a;
    --paper: #ffffff;
    --band-light: #e6f0f7;
    --band-mid: #c9dcea;
    --skin-tone: #d9b8a2;
  }
  * { box-sizing: border-box; margin: 0; padding: 0; }
  html, body {
    width: 1200px;
    height: 900px;
    overflow: hidden;
    background: var(--backdrop);
  }
  .canvas {
    position: relative;
    width: 1200px;
    height: 900px;
  }
  .card {
    position: absolute;
    top: 322px;
    width: 371px;
    height: 212px;
    overflow: hidden;
  }

  /* Front side */
  .card--front {
    left: 168px;
    background: var(--brand-blue);
  }
  .front-mark {
    position: absolute;
    top: 0;
    left: 0;
    width: 100%;
    height: 134px;
    display: flex;
    align-items: center;
    justify-content: center;
    gap: 8px;
  }
  .front-mark__dot {
    width: 14px;
    height: 14px;
    border-radius: 50%;
    background: var(--paper);
  }
  .front-mark__name {
    font-family: "Fira Sans", sans-serif;
    font-weight: 300;
    font-size: 17px;
    color: var(--paper);
    letter-spacing: 0.2px;
  }
  .banner-photo {
    position: absolute;
    top: 134px;
    left: 0;
    width: 100%;
    height: 62px;
    background: linear-gradient(90deg, var(--band-light) 0%, var(--band-mid) 40%, var(--skin-tone) 62%, var(--band-mid) 85%, var(--band-light) 100%);
  }

  /* Back side */
  .card--back {
    left: 656px;
    background: var(--paper);
  }
  .back-mark {
    position: absolute;
    left: 20px;
    top: 94px;
    display: flex;
    align-items: center;
    gap: 9px;
  }
  .back-mark__dot {
    width: 34px;
    height: 34px;
    border-radius: 50%;
    background: var(--brand-red);
    flex: none;
  }
  .back-mark__name {
    font-family: "Fira Sans", sans-serif;
    font-weight: 300;
    font-size: 18px;
    line-height: 24px;
    color: var(--brand-blue);
  }
  .contact {
    position: absolute;
    left: 219px;
    top: 58px;
    width: 140px;
    font-family: "Jost", sans-serif;
  }
  .contact__title {
    font-size: 15px;
    font-weight: 500;
    color: var(--brand-red);
    margin-bottom: 10px;
  }
  .contact__list {
    list-style: none;
    font-size: 8.5px;
    line-height: 11px;
    color: var(--ink);
  }
  .contact__label { color: var(--brand-red); }
  .contact__tagline {
    margin-top: 11px;
    font-size: 8.5px;
    line-height: 10.5px;
    color: var(--brand-red);
  }
</style>
</head>
<body>
  <main class="canvas">
    <section class="card card--front" aria-label="Business card front">
      <div class="front-mark">
        <span class="front-mark__dot"></span>
        <span class="front-mark__name">Healer at the Hearth</span>
      </div>
      <div class="banner-photo" role="img" aria-label="Banner photo of a clinician's hands gently holding a patient's hand"></div>
    </section>

    <section class="card card--back" aria-label="Business card back">
      <div class="back-mark">
        <span class="back-mark__dot"></span>
        <span class="back-mark__name">Healer at<br>the Hearth</span>
      </div>
      <div class="contact">
        <h1 class="contact__title">Title here</h1>
        <ul class="contact__list">
          <li><span class="contact__label">tel:</span> +01 12 3456 7890</li>
          <li><span class="contact__label">email:</span> mail@myid.com</li>
          <li><span class="contact__label">web:</span> www.healerathearth.ca</li>
        </ul>
        <p class="contact__tagline">Tagline here,tagline here tagline here</p>
      </div>
    </section>
  </main>
</body>
</html>
```